" Escritório de advocacia formado por advogados jovens, altamente motivados por resultados, que são parceiros dos clientes na resolução dos problemas. Esse perfil agressivo, arrojado, inquieto, vibrante, deve ser refletido no projeto e material de comunicação. "

```html
<!DOCTYPE html>
<html lang="pt-BR">
<head>
<meta charset="UTF-8">
<title>Serra Alta Advogados</title>
<link href="https://fonts.googleapis.com/css2?family=Montserrat:wght@500;700&display=swap" rel="stylesheet">
<style>
  :root {
    --page-bg: #e9e6e1;
    --sky-gold: #e9b35c;
    --sky-amber: #c98a45;
    --haze: #8f7f6c;
    --ridge: #3c4650;
    --night: #1e2730;
    --text-light: #ffffff;
    --text-soft: rgba(255,255,255,0.72);
    --brand-beige: #efe3c2;
  }
  * { margin: 0; padding: 0; box-sizing: border-box; }
  html, body {
    width: 1200px; height: 1200px; overflow: hidden;
    background: var(--page-bg);
    font-family: "Montserrat", sans-serif;
  }
  .site-hero {
    position: absolute; left: 0; top: 225px;
    width: 1200px; height: 750px;
    overflow: hidden;
    color: var(--text-light);
  }
  .hero-photo {
    position: absolute; inset: 0;
    background:
      radial-gradient(ellipse 45% 30% at 42% 28%, rgba(255,226,150,0.95), rgba(233,179,92,0) 70%),
      linear-gradient(180deg, #7d6a55 0%, var(--sky-amber) 18%, var(--sky-gold) 34%, var(--haze) 52%, var(--ridge) 70%, var(--night) 100%);
  }
  .site-nav {
    position: absolute; top: 40px; left: 330px;
    display: flex; gap: 44px;
    font-size: 13px; font-weight: 700; letter-spacing: 0.08em;
  }
  .site-nav span::after { content: " ▾"; font-size: 9px; }
  .brand {
    position: absolute; left: 70px; top: 150px;
    display: flex; align-items: center; gap: 14px;
    font-size: 18px; font-weight: 700; letter-spacing: 0.06em;
    color: var(--brand-beige);
  }
  .brand-square { width: 46px; height: 46px; background: var(--brand-beige); }
  .hero-headline {
    position: absolute; left: 70px; top: 450px; width: 1000px;
    font-size: 29px; font-weight: 700; line-height: 1.3;
    letter-spacing: 0.06em; text-transform: uppercase;
  }
  .social-note {
    position: absolute; right: 70px; top: 470px;
    font-size: 10px; font-weight: 500; letter-spacing: 0.12em;
    color: var(--text-soft); text-transform: uppercase;
  }
  .site-footer {
    position: absolute; left: 0; right: 0; bottom: 40px;
    text-align: center; font-size: 10px; font-weight: 500;
    letter-spacing: 0.08em; color: var(--text-soft);
  }
</style>
</head>
<body>
  <section class="site-hero">
    <div class="hero-photo" role="img" aria-label="Foto ao pôr do sol: pessoa de pé no alto de uma montanha olhando o vale enevoado"></div>

    <nav class="site-nav">
      <span>EMPRESA</span>
      <span>ESPECIALIDADES</span>
      <span>CASES</span>
      <span>CONTEÚDO</span>
      <span>FALE CONOSCO</span>
    </nav>

    <div class="brand">
      <div class="brand-square"></div>
      <span>SERRA ALTA ADVOGADOS</span>
    </div>

    <h1 class="hero-headline">Somos especializados em assessorar<br>famílias, empresas e empreendedores<br>de sucesso na realização de seus negócios.</h1>

    <div class="social-note">Redes sociais</div>

    <footer class="site-footer">© 2024 Serra Alta Advogados · Todos os direitos reservados</footer>
  </section>
</body>
</html>
```